Tales from Kin Logo Design plus business cards design

We are a start up company that will help seniors write their memoirs...beginning with a few ancestors and their heritage and continuing through their own history...how they would like to be remembered in the next generation. I envision a card with a senior citizen at an older writing desk, writing her memoirs, with a book (maybe standing on top, leaning slightly) that has the words Tales from Kin.com on the back binding. OR maybe a senior couple walking into the sunset with the same book somewhere in the frame. Communicating the relevance of every life being significant to those that come after them...when a genealogy doesn't say enough about the details of ones life. Please note that I am open to the professionals own ideas...I am not locked into my concepts. On the back of the card I would like one or two phrases..."A Genealogy Doesn't Say Enough" and/or "Every life legacy is uniquely significant to the next generation".
Updates

I have added a couple of photos for ideas that may be used if needed.

I have both increased and committed the payment! Thanks for the reminder!

Reason: We increased the payment commitment and added some photo ideas to help.

We want to thank EVERYONE who participated in this contest. There were so many wonderful and VERY professional proposals...making it very challenging to decide on one! We are posting a new contest for a brochure now and hope many of you will participate. May God bless your endeavors.

Target Market(s)

Senior populous & baby boomer generation.

Industry/Entity Type

Business

Logo Text

Tales from Kin ordinary lives...extraordinary legacy

Requirements
Must have
• Relevant info:
Domain name: talesfromkin.com
email: info@talesfromkin.com
phone: 1-855-GAB-TALE toll free
1-717-382-5619 local
name: Doris Whitlock, M.A.
Nice to have
• photo of senior or senior couple....book with our web address on the binding. I attached two photos that could work if cropped and enhanced. Words need to be deleted from the one photo of senior at a writing desk and couple on the beach could use a sunset sky and other people cropped out. Just ideas...don't know if you have better ones or prefer a different idea.

```html
<!DOCTYPE html>
<html lang="en">
<head>
<meta charset="utf-8">
<title>Tales from Kin – Business Cards</title>
<link rel="stylesheet" href="https://fonts.googleapis.com/css2?family=Source+Sans+3:ital,wght@0,400;0,600;1,400&display=swap">
<style>
  :root {
    --page: #ffffff;
    --ink: #1e1e1e;
    --brand-brown: #3a2a1c;
    --photo-dark: #17110b;
    --photo-mid: #4a3521;
    --photo-warm: #6b4c2e;
    --card-white: #ffffff;
    --on-photo: #ffffff;
    --on-photo-soft: #eadfce;
    --shadow: rgba(0, 0, 0, 0.35);
  }
  * { box-sizing: border-box; margin: 0; padding: 0; }
  html, body {
    width: 1200px;
    height: 900px;
    overflow: hidden;
    background: var(--page);
    font-family: "Source Sans 3", "Helvetica Neue", Arial, sans-serif;
    color: var(--ink);
  }
  .sheet {
    position: relative;
    width: 1200px;
    height: 900px;
  }
  .sheet-wordmark {
    position: absolute;
    left: 40px;
    top: 36px;
    font-size: 26px;
    font-weight: 600;
    color: var(--brand-brown);
    letter-spacing: 0.5px;
  }
  .card {
    position: absolute;
    left: 320px;
    width: 560px;
    height: 320px;
    overflow: hidden;
    background: var(--card-white);
    box-shadow: 4px 6px 10px var(--shadow);
  }
  .card--front { top: 110px; }
  .card--back  { top: 480px; }

  .card-photo {
    position: absolute;
    left: 0;
    top: 0;
    width: 100%;
  }
  .card--front .card-photo {
    height: 100%;
    background: radial-gradient(ellipse at 35% 70%, var(--photo-warm) 0%, var(--photo-mid) 35%, var(--photo-dark) 80%);
  }
  .card--back .card-photo {
    height: 148px;
    background: radial-gradient(ellipse at 65% 60%, var(--photo-mid) 0%, var(--photo-dark) 70%);
  }

  .front-name {
    position: absolute;
    left: 0;
    right: 0;
    top: 128px;
    text-align: center;
    font-size: 52px;
    font-weight: 400;
    color: var(--on-photo);
    letter-spacing: 0.5px;
  }

  .back-tagline {
    position: absolute;
    right: 50px;
    top: 48px;
    width: 300px;
    text-align: center;
    font-style: italic;
    font-size: 16px;
    line-height: 1.4;
    color: var(--on-photo-soft);
  }

  .back-contact {
    position: absolute;
    right: 40px;
    top: 166px;
    text-align: right;
    font-size: 15px;
    line-height: 1.35;
    color: var(--ink);
  }
  .contact-name {
    font-size: 20px;
    font-weight: 600;
    margin-bottom: 6px;
  }
</style>
</head>
<body>
  <main class="sheet">
    <div class="sheet-wordmark">Tales from Kin</div>

    <section class="card card--front" aria-label="Business card front">
      <div class="card-photo" role="img" aria-label="Sepia-toned close-up photograph of a vintage typewriter keyboard"></div>
      <div class="front-name">Tales from Kin</div>
    </section>

    <section class="card card--back" aria-label="Business card back">
      <div class="card-photo" role="img" aria-label="Dark sepia photograph of typewriter type bars"></div>
      <p class="back-tagline">Every life legacy is uniquely significant to the next generation</p>
      <div class="back-contact">
        <p class="contact-name">Doris Whitlock, M.A.</p>
        <p>1-855-GAB-TALE toll free</p>
        <p>1-717-382-5619 local</p>
        <p>info@talesfromkin.com</p>
        <p>www.talesfromkin.com</p>
      </div>
    </section>
  </main>
</body>
</html>
```